lunavo GmbH needs great looking businesscards to leave an impression

Dear Designers,

Our company lunavo GmbH based in switzerland needs to have impressive businesscards. We produce and sell high quality bleaching products for the upper market.
We'd like to have a minimalistic but still meaningful design. You'll fine our company logo attached and some of our packaging designs. Our company slogan is "reveal your bright side". If you need additional information feel free to contact us.
Kind Regards Milo

Dear Designers, This is a business card design contest! I try to call the support to fix that. Kind Regards Milo

```html
<!DOCTYPE html>
<html lang="de">
<head>
<meta charset="utf-8">
<title>lunavo GmbH – Visitenkarte</title>
<link href="https://fonts.googleapis.com/css2?family=PT+Sans:wght@400;700&display=swap" rel="stylesheet">
<style>
  :root {
    --bg: #c9cbcd;
    --card: #efefef;
    --teal: #1e5a60;
    --coral: #e8877c;
    --ink: #4f5152;
    --faint: #e2e2e2;
  }
  * { margin: 0; padding: 0; box-sizing: border-box; }
  html, body { width: 1200px; height: 900px; overflow: hidden; }
  body {
    background: var(--bg);
    font-family: "PT Sans", Arial, sans-serif;
    display: flex;
    align-items: center;
    justify-content: center;
    gap: 40px;
  }
  .card {
    position: relative;
    width: 520px;
    height: 312px;
    background: var(--card);
    border-radius: 26px;
    overflow: hidden;
  }
  /* Front side */
  .front .brand {
    position: absolute;
    right: 34px;
    top: 128px;
    text-align: right;
  }
  .brand-row {
    display: flex;
    align-items: center;
    justify-content: flex-end;
    gap: 10px;
  }
  .brand-name {
    color: var(--teal);
    font-weight: 400;
    letter-spacing: 0.08em;
    white-space: nowrap;
  }
  .front .brand-name { font-size: 44px; }
  .brand-dot {
    border-radius: 50%;
    background: var(--teal);
    flex: none;
  }
  .front .brand-dot { width: 56px; height: 56px; }
  .slogan {
    color: var(--coral);
    font-size: 17px;
    letter-spacing: 0.12em;
    margin-top: 2px;
    margin-right: 66px;
    white-space: nowrap;
  }
  /* Back side */
  .back .brand {
    position: absolute;
    left: 36px;
    top: 40px;
  }
  .back .brand-row { justify-content: flex-start; }
  .back .brand-name { font-size: 34px; }
  .back .brand-dot { width: 34px; height: 34px; }
  .decor-circle {
    position: absolute;
    right: 46px;
    top: 64px;
    width: 180px;
    height: 180px;
    border-radius: 50%;
    background: var(--faint);
  }
  .contact {
    position: absolute;
    left: 38px;
    top: 108px;
    white-space: nowrap;
  }
  .person-name { color: var(--coral); font-size: 20px; line-height: 1.1; }
  .person-title { color: var(--coral); font-size: 12px; margin-bottom: 16px; }
  .address { color: var(--ink); font-size: 14px; line-height: 1.3; margin-bottom: 16px; }
  .lines { font-size: 14px; line-height: 1.3; color: var(--teal); }
  .label { color: var(--coral); }
</style>
</head>
<body>
  <section class="card front" aria-label="Vorderseite">
    <div class="brand">
      <div class="brand-row">
        <span class="brand-name">lunavo</span>
        <span class="brand-dot"></span>
      </div>
      <div class="slogan">reveal your bright side</div>
    </div>
  </section>

  <section class="card back" aria-label="Rückseite">
    <div class="decor-circle"></div>
    <div class="brand">
      <div class="brand-row">
        <span class="brand-name">lunavo</span>
        <span class="brand-dot"></span>
      </div>
    </div>
    <div class="contact">
      <div class="person-name">Jonas Berner</div>
      <div class="person-title">Mister</div>
      <div class="address">lunavo GmbH<br>Lindenweg 14<br>3011 Bern</div>
      <div class="lines">
        <div><span class="label">[M]</span> 0041 79 000 45 67</div>
        <div><span class="label">[E]</span> jonas.berner@mailbox.ch</div>
      </div>
    </div>
  </section>
</body>
</html>
```